Business Cards

Business card design for my company.
I would like the card's background colour to be black. You can also see our web site to get an idea of our brand. https://www.dlqmarrowfield.com.au/
- Name
- Email

```html
<!DOCTYPE html>
<html lang="en">
<head>
<meta charset="utf-8">
<title>DLQ Marrowfield – Business Cards</title>
<link href="https://fonts.googleapis.com/css2?family=Montserrat:wght@500;600;800&display=swap" rel="stylesheet">
<style>
  :root {
    --stage: #b3b4b3;
    --card: #111111;
    --green: #10953f;
    --white: #f4f4f4;
    --gold: #c99a3a;
    --silver: #b9bbbd;
    --charcoal: #2c2c2c;
    --orange: #f2a21a;
    --blue: #2a56a8;
  }
  * { box-sizing: border-box; margin: 0; padding: 0; }
  html, body { width: 1200px; height: 939px; overflow: hidden; }
  body {
    background: var(--stage);
    font-family: "Montserrat", sans-serif;
    color: var(--white);
    position: relative;
  }
  .card {
    position: absolute;
    width: 560px;
    height: 320px;
    background: var(--card);
    border-bottom: 3px solid var(--green);
    border-left: 3px solid var(--green);
    box-shadow: 0 10px 24px rgba(0,0,0,.25);
  }
  .card--front { left: 120px; top: 90px; }
  .card--back { left: 520px; top: 520px; }

  .wordmark {
    display: flex;
    align-items: center;
    gap: 12px;
    font-weight: 800;
    color: var(--white);
    letter-spacing: .04em;
    text-transform: uppercase;
    line-height: 1;
    white-space: nowrap;
  }
  .wordmark__square { background: var(--green); flex: none; }
  .card--front .wordmark {
    position: absolute; left: 0; right: 0; top: 140px;
    justify-content: center; font-size: 34px;
  }
  .card--front .wordmark__square { width: 28px; height: 28px; }

  .card--back .wordmark {
    position: absolute; left: 30px; top: 128px; font-size: 16px; gap: 8px;
  }
  .card--back .wordmark__square { width: 15px; height: 15px; }

  .divider {
    position: absolute; left: 266px; top: 44px;
    width: 1.5px; height: 168px; background: var(--white);
  }
  .contact { position: absolute; left: 284px; top: 44px; right: 16px; }
  .contact__name {
    font-weight: 800; font-size: 27px; letter-spacing: .02em;
    text-transform: uppercase; line-height: 1.05; white-space: nowrap;
  }
  .contact__role {
    color: var(--green); font-weight: 600; font-size: 14px;
    letter-spacing: .04em; margin: 4px 0 12px;
  }
  .contact__list { list-style: none; }
  .contact__item {
    display: flex; align-items: center; gap: 9px;
    font-size: 12.5px; font-weight: 500; letter-spacing: .03em;
    height: 24px; white-space: nowrap;
  }
  .contact__icon { width: 12px; height: 12px; flex: none; fill: var(--green); }

  .awards {
    position: absolute; left: 34px; right: 24px; bottom: 24px;
    display: flex; justify-content: space-between; list-style: none;
  }
  .award { width: 40px; height: 40px; border-radius: 50%; border: 2px solid rgba(255,255,255,.35); }
  .award--gold { background: var(--gold); }
  .award--silver { background: var(--silver); }
  .award--charcoal { background: var(--charcoal); }
  .award--orange { background: var(--orange); }
  .award--blue { background: var(--white); border: 3px solid var(--blue); }
</style>
</head>
<body>
  <section class="card card--front" aria-label="Business card front">
    <div class="wordmark"><span class="wordmark__square"></span>DLQ Marrowfield</div>
  </section>

  <section class="card card--back" aria-label="Business card back">
    <div class="wordmark"><span class="wordmark__square"></span>DLQ Marrowfield</div>
    <div class="divider"></div>
    <div class="contact">
      <h1 class="contact__name">Owen Hartley</h1>
      <p class="contact__role">General Manager</p>
      <ul class="contact__list">
        <li class="contact__item">
          <svg class="contact__icon" viewBox="0 0 24 24"><path d="M6.6 10.8a15.1 15.1 0 0 0 6.6 6.6l2.2-2.2a1 1 0 0 1 1-.25 11.4 11.4 0 0 0 3.6.57 1 1 0 0 1 1 1V20a1 1 0 0 1-1 1A17 17 0 0 1 3 4a1 1 0 0 1 1-1h3.5a1 1 0 0 1 1 1c0 1.25.2 2.45.57 3.57a1 1 0 0 1-.25 1z"/></svg>
          0400 555 018
        </li>
        <li class="contact__item">
          <svg class="contact__icon" viewBox="0 0 24 24"><path d="M2 5h20v14H2z M4 7v.5l8 5 8-5V7l-8 5z" fill-rule="evenodd"/></svg>
          info@dlqmarrowfield.com.au
        </li>
        <li class="contact__item">
          <svg class="contact__icon" viewBox="0 0 24 24"><path d="M12 2a10 10 0 1 0 0 20 10 10 0 0 0 0-20zm6.9 6h-3a15.7 15.7 0 0 0-1.4-3.6A8 8 0 0 1 18.9 8zM12 4c.8 1.2 1.5 2.5 1.9 4h-3.8c.4-1.5 1.1-2.8 1.9-4zM4.3 14a8.2 8.2 0 0 1 0-4h3.4a16.5 16.5 0 0 0 0 4zm.8 2h3a15.7 15.7 0 0 0 1.4 3.6A8 8 0 0 1 5.1 16zm3-8h-3a8 8 0 0 1 4.4-3.6A15.7 15.7 0 0 0 8.1 8zM12 20c-.8-1.2-1.5-2.5-1.9-4h3.8c-.4 1.5-1.1 2.8-1.9 4zm2.3-6H9.7a14.7 14.7 0 0 1 0-4h4.6a14.7 14.7 0 0 1 0 4zm.2 5.6a15.7 15.7 0 0 0 1.4-3.6h3a8 8 0 0 1-4.4 3.6zm1.8-5.6a16.5 16.5 0 0 0 0-4h3.4a8.2 8.2 0 0 1 0 4z"/></svg>
          www.dlqmarrowfield.com.au
        </li>
        <li class="contact__item">
          <svg class="contact__icon" viewBox="0 0 24 24"><path d="M12 2a7 7 0 0 0-7 7c0 5.2 7 13 7 13s7-7.8 7-13a7 7 0 0 0-7-7zm0 9.5A2.5 2.5 0 1 1 12 6.5a2.5 2.5 0 0 1 0 5z"/></svg>
          Fernhollow, Westmere, Calverra
        </li>
      </ul>
    </div>
    <ul class="awards" aria-label="Industry award badges">
      <li class="award award--gold"></li>
      <li class="award award--charcoal"></li>
      <li class="award award--silver"></li>
      <li class="award award--gold"></li>
      <li class="award award--gold"></li>
      <li class="award award--charcoal"></li>
      <li class="award award--silver"></li>
      <li class="award award--orange"></li>
      <li class="award award--charcoal"></li>
      <li class="award award--blue"></li>
    </ul>
  </section>
</body>
</html>
```